Modifications to a letterhead design

The following changes are being made to show other options for staff. Thanks

Part A - Letterhead
I have the two letterheads that I need a slight change made. I have already turned them into templates. So I hope the changes to the design can still occur.
Where the school name is, could you remove the yellow line and brown shape. Instead, please write:

Brell Tanner Ridge High School

The colour is to be in the chocolate brown colour. The font size and positioning for the school name can stay the same.

Changes to occur for colour and black&white

Part B - Certificates

Principal Award:
- Where the school name is, could you remove the yellow line and brown shape. Instead, please write: Brell Tanner Ridge High School
The colour is to be in the chocolate brown colour. The font size remains the same and it needs to be centred on the page
- Please remove the purple box and have no box
- for the 5 award categories please have not dot before the word, and centre the 5 categories and ensure the first letter is in capitals but the rest of the letters are lower case, for example: School Service
- Please remove the principal banner and change to ribbon on page 2 of the slide show - you will need to tidy it up or create new as I just cut and pasted it
- then could I have 2 Principal Awards - one addressing the above, and a second one addressing those things mentioned above plus removing all the colour at the bottom of the page

Year Advisor Award
- Use the same template design for the Principal Award mentioned above (including the details mentioned above). This time change the name on the ribbon (on page 2 of powerpoint) to Year Adviser's Award (only fist letter is capital , the rest lower case).
- Also, for the Year Adviser's Award, please produce 5 certificates with 1 category on each certificate e.g. School Service (again only first letter in capitals, the rest lower case). Also, the 5 certificates have a changed colour at the bottom of the page (including the 3 twirling ribbons). Colours for the bottom of the certificates are: Green, purple, red, yellow and blue.
- Please also create the 5 Year Adviser certificates without any colour at the bottom as well

```html
<!DOCTYPE html>
<html lang="en">
<head>
<meta charset="utf-8">
<title>Brell Tanner Ridge High School – Letterhead</title>
<link href="https://fonts.googleapis.com/css2?family=Tinos:ital,wght@0,400;1,700&family=Arimo:wght@400&display=swap" rel="stylesheet">
<style>
  :root {
    --chocolate: #3a1a1c;
    --purple: #8e3f95;
    --purple-soft: #a158a7;
    --yellow: #f2e21a;
    --ink: #1f1f1f;
    --paper: #ffffff;
  }
  html, body { margin: 0; padding: 0; overflow: hidden; background: var(--paper); }
  .letterhead {
    position: relative;
    width: 928px;
    height: 1200px;
    overflow: hidden;
    background: var(--paper);
    font-family: "Arimo", Arial, sans-serif;
    color: var(--ink);
  }
  .top-band {
    position: absolute;
    top: 0; left: 0;
    width: 928px;
    height: 44px;
    background: linear-gradient(90deg, var(--purple) 0%, var(--chocolate) 55%, var(--purple) 80%, var(--yellow) 100%);
  }
  .crest {
    position: absolute;
    left: 42px;
    top: 68px;
    width: 114px;
    text-align: center;
  }
  .crest-mark {
    width: 72px; height: 72px;
    margin: 0 auto 6px;
    border-radius: 50%;
    background: var(--purple);
  }
  .crest-name {
    font-family: "Tinos", "Times New Roman", serif;
    font-size: 12px;
    line-height: 1.2;
    color: var(--chocolate);
  }
  .school-name {
    position: absolute;
    left: 181px;
    top: 80px;
    margin: 0;
    font-family: "Tinos", "Times New Roman", serif;
    font-weight: 400;
    font-size: 25px;
    color: var(--chocolate);
    white-space: nowrap;
  }
  .principal {
    position: absolute;
    left: 181px;
    top: 122px;
    margin: 0;
    font-size: 11.3px;
    line-height: 15px;
    color: var(--ink);
  }
  .motto {
    position: absolute;
    left: 181px;
    top: 161px;
    margin: 0;
    font-family: "Tinos", "Times New Roman", serif;
    font-style: italic;
    font-weight: 700;
    font-size: 14.5px;
    color: var(--ink);
  }
  .contacts {
    position: absolute;
    left: 606px;
    top: 54px;
    margin: 0;
    padding: 0;
    list-style: none;
  }
  .contacts li {
    display: flex;
    align-items: center;
    height: 20px;
    font-size: 12px;
    color: var(--ink);
    white-space: nowrap;
  }
  .contact-icon {
    width: 16px; height: 16px;
    margin-right: 10px;
    flex: none;
  }
  .footer-address {
    position: absolute;
    left: 236px;
    top: 1127px;
    display: flex;
    align-items: center;
    font-size: 18px;
    color: var(--ink);
    white-space: pre;
  }
  .footer-address svg { margin-right: 6px; }
</style>
</head>
<body>
<div class="letterhead">
  <div class="top-band" role="img" aria-label="Decorative purple, brown and yellow banner across the top of the page"></div>

  <div class="crest">
    <div class="crest-mark"></div>
    <div class="crest-name">Brell Tanner Ridge</div>
  </div>

  <h1 class="school-name">Brell Tanner Ridge High School</h1>
  <p class="principal">Principal: Ms Dana Whitlow BEd (UP/LS),<br>GCertEd, PGCertEdLead, GCertDisSt, MEd(SpecEd), NSW JP</p>
  <p class="motto">“For so much, what shall we repay?”</p>

  <ul class="contacts">
    <li><svg class="contact-icon" viewBox="0 0 16 16" aria-hidden="true"><circle cx="8" cy="8" r="8" fill="var(--purple-soft)"/><path fill="#fff" d="M5.2,4 L6.6,4 L7.2,6 L6.3,6.8 C6.8,7.9 7.7,8.8 8.9,9.4 L9.7,8.5 L11.6,9.1 L11.6,10.6 C11.6,11.2 11,11.7 10.3,11.6 C7.2,11.2 4.7,8.7 4.3,5.5 C4.2,4.7 4.6,4 5.2,4 Z"/></svg>02 5550 1408</li>
    <li><svg class="contact-icon" viewBox="0 0 16 16" aria-hidden="true"><circle cx="8" cy="8" r="8" fill="var(--purple-soft)"/><rect x="5" y="6" width="6" height="5" fill="none" stroke="#fff" stroke-width="1"/><rect x="6" y="4" width="4" height="2" fill="#fff"/></svg>02 5550 1223</li>
    <li><svg class="contact-icon" viewBox="0 0 16 16" aria-hidden="true"><circle cx="8" cy="8" r="8" fill="var(--purple-soft)"/><rect x="4.5" y="5.5" width="7" height="5" fill="none" stroke="#fff" stroke-width="1"/><path d="M4.5,5.5 L8,8.3 L11.5,5.5" fill="none" stroke="#fff" stroke-width="1"/></svg>brelltanner-h.school@example.edu.au</li>
    <li><svg class="contact-icon" viewBox="0 0 16 16" aria-hidden="true"><circle cx="8" cy="8" r="8" fill="var(--purple-soft)"/></svg>http://btrhs.portal.example.au</li>
    <li><svg class="contact-icon" viewBox="0 0 16 16" aria-hidden="true"><circle cx="8" cy="8" r="8" fill="var(--purple-soft)"/></svg>https://social.example.com/brelltannerhigh</li>
    <li><svg class="contact-icon" viewBox="0 0 16 16" aria-hidden="true"><circle cx="8" cy="8" r="8" fill="var(--purple-soft)"/><rect x="4.5" y="5" width="7" height="5" rx="1" fill="none" stroke="#fff" stroke-width="1"/><path d="M7,11.5 H9" stroke="#fff" stroke-width="1"/></svg>https://brelltanner-h.schools.example.au</li>
    <li><svg class="contact-icon" viewBox="0 0 16 16" aria-hidden="true"><circle cx="8" cy="8" r="8" fill="var(--purple-soft)"/></svg>https://video.example.com/user40218857</li>
  </ul>

  <div class="footer-address">
    <svg width="40" height="40" viewBox="0 0 40 40" aria-hidden="true">
      <circle cx="20" cy="20" r="20" fill="var(--chocolate)"/>
      <path fill="#fff" d="M20,9 C15.6,9 12.5,12.2 12.5,16.3 C12.5,21.5 20,30 20,30 C20,30 27.5,21.5 27.5,16.3 C27.5,12.2 24.4,9 20,9 Z"/>
      <circle cx="20" cy="16.2" r="3" fill="var(--chocolate)"/>
    </svg>PO Box 418 BRELL  NSW  2799  -  ABN: 47 615 203 948</div>
</div>
</body>
</html>
```